PELDRAX Business Cards

We require a business card for our company that provides IT consulting services. We already have a logo that needs to be used on the card. We want a clean professional looking design that incorporates our colours. Our main focus is providing managed services to business, which involves us looking after all of their IT requirements including managing servers/networks, projects, and procurement.

Industry/Entity Type

Information Technology

Requirements
Must have
• our logo, contact information, name, title, phone numbers

```html
<!DOCTYPE html>
<html lang="en">
<head>
<meta charset="utf-8">
<title>PELDRAX Business Card</title>
<link rel="stylesheet" href="https://fonts.googleapis.com/css2?family=Open+Sans:wght@400;600&display=swap">
<style>
  :root {
    --page-bg: #e4e6e9;
    --card-bg: #f4f5f6;
    --brand-blue: #3d82c4;
    --band-blue: #4a86c5;
    --pattern-tint: #e3ebf3;
    --ink: #1d1d1f;
    --ink-soft: #3a3a3c;
    --rule: #6b6b6e;
    --white: #ffffff;
  }
  * { box-sizing: border-box; margin: 0; padding: 0; }
  html, body { width: 1200px; height: 922px; overflow: hidden; }
  body {
    background: var(--page-bg);
    font-family: "Open Sans", Arial, sans-serif;
    position: relative;
  }
  .card {
    position: absolute;
    left: 280px;
    width: 640px;
    height: 366px;
    background: var(--card-bg);
    box-shadow: 0 6px 18px rgba(0,0,0,0.18);
    overflow: hidden;
  }
  .card--back { top: 64px; }
  .card--front { top: 486px; }

  /* Back */
  .back-pattern {
    position: absolute; inset: 0;
    background: linear-gradient(135deg, var(--pattern-tint), #eef2f6);
  }
  .brand {
    position: absolute;
    display: flex; align-items: center; gap: 12px;
    color: var(--brand-blue);
    font-weight: 600;
    letter-spacing: 2px;
  }
  .brand-square {
    display: block; background: var(--brand-blue);
  }
  .card--back .brand {
    left: 50%; top: 50%; transform: translate(-50%, -50%);
    font-size: 40px;
  }
  .card--back .brand-square { width: 34px; height: 34px; }

  /* Front */
  .card--front .brand {
    left: 52px; top: 132px;
    font-size: 44px;
  }
  .card--front .brand-square { width: 40px; height: 40px; }
  .divider {
    position: absolute;
    left: 378px; top: 34px;
    width: 1px; height: 226px;
    background: var(--rule);
  }
  .person { position: absolute; left: 402px; top: 40px; }
  .person-name { font-size: 22px; color: var(--ink); font-weight: 400; line-height: 1.2; }
  .person-title { font-size: 15px; color: var(--ink-soft); margin-left: 12px; }
  .contacts {
    position: absolute; left: 418px; top: 128px;
    list-style: none;
    font-size: 15px; color: var(--ink); line-height: 24px;
  }
  .contacts li { display: flex; align-items: center; gap: 10px; }
  .contacts svg { width: 14px; height: 14px; flex: none; }
  .tagline-band {
    position: absolute; left: 0; right: 0; bottom: 0;
    height: 54px;
    background: var(--band-blue);
    color: var(--white);
    font-size: 19px;
    display: flex; align-items: center; justify-content: center;
    letter-spacing: 0.3px;
  }
</style>
</head>
<body>

<section class="card card--back" aria-label="Card back">
  <div class="back-pattern" role="img" aria-label="Faint repeating brand pattern in pale blue"></div>
  <div class="brand"><span class="brand-square"></span>PELDRAX</div>
</section>

<section class="card card--front" aria-label="Card front">
  <div class="brand"><span class="brand-square"></span>PELDRAX</div>
  <div class="divider"></div>
  <div class="person">
    <p class="person-name">Marten Hale</p>
    <p class="person-title">Manager</p>
  </div>
  <ul class="contacts">
    <li>
      <svg viewBox="0 0 14 14"><rect width="14" height="14" rx="2" fill="var(--brand-blue)"/><rect x="4.5" y="2.5" width="5" height="9" rx="1" fill="none" stroke="#fff" stroke-width="1.2"/></svg>
      +01 555 014 282
    </li>
    <li>
      <svg viewBox="0 0 14 14"><rect width="14" height="14" rx="2" fill="var(--brand-blue)"/><path d="M4 3.5c1 0 1.4 1.6 1.1 2.1-.3.4-.6.5-.3 1.1.6 1 1.3 1.7 2.3 2.2.5.3.7 0 1-.3.5-.4 2 .2 2 1.1 0 .8-1 1.2-1.8 1-2.6-.6-4.6-2.7-5.2-5.3C3 4.5 3.4 3.5 4 3.5z" fill="#fff"/></svg>
      +01 555 014 283
    </li>
    <li>
      <svg viewBox="0 0 14 14"><rect width="14" height="14" rx="2" fill="var(--brand-blue)"/><rect x="2.5" y="4" width="9" height="6.5" fill="none" stroke="#fff" stroke-width="1.1"/><path d="M2.5 4l4.5 3.6L11.5 4" fill="none" stroke="#fff" stroke-width="1.1"/></svg>
      info@PELDRAX.com
    </li>
    <li>
      <svg viewBox="0 0 14 14"><rect width="14" height="14" rx="2" fill="var(--brand-blue)"/><circle cx="7" cy="7" r="4.2" fill="none" stroke="#fff" stroke-width="1.1"/><path d="M2.8 7h8.4M7 2.8c-2 2.4-2 6 0 8.4M7 2.8c2 2.4 2 6 0 8.4" fill="none" stroke="#fff" stroke-width="0.9"/></svg>
      www.PELDRAX.com
    </li>
  </ul>
  <div class="tagline-band">Managing servers/networks, projects, and procurement</div>
</section>

</body>
</html>
```